Stationary & Business Cards
TRB Weddings & Events by Greta
You need to extend the project before designers can submit more proposals, right now it is locked. Thank you! :)
And we need business cards, stationary & envelopes.
They like a zen feel...cherry blossoms...birds...
Thank you for all of your submissions. The owners do not like the purple logo anymore and have completly changed it. We have uploaded a eps file for it. This project is guaranteed and we will be picking a winner. If you have time please submit new designs. Thank you.
Your eps file is an image please upload orignal Ai file.
-Thanks
Please upload ai or eps of your logo.

```html
<!DOCTYPE html>
<html lang="en">
<head>
<meta charset="utf-8">
<title>TRB Weddings &amp; Events by Greta – Stationery Set</title>
<link rel="stylesheet" href="https://fonts.googleapis.com/css2?family=Crimson+Text:wght@600;700&family=Open+Sans:wght@400;700&display=swap">
<style>
  :root {
    --leaf: #8fc043;
    --leaf-light: #c9e295;
    --leaf-pale: #e6f1d0;
    --leaf-dark: #4f8f22;
    --ink: #5c5c5c;
    --muted: #8a8a8a;
    --paper: #ffffff;
    --edge: #b9d88a;
    --frame: #1a1a1a;
  }
  * { box-sizing: border-box; margin: 0; padding: 0; }
  html, body { width: 1200px; height: 830px; overflow: hidden; background: var(--paper); }
  .sheet {
    position: relative; width: 1200px; height: 830px;
    font-family: "Open Sans", Arial, sans-serif; color: var(--ink);
  }
  .sheet-frame { position: absolute; inset: 10px; border: 2px solid var(--frame); }
  .piece {
    position: absolute; background: var(--paper); border: 1px solid var(--edge); overflow: hidden;
  }
  .band {
    position: absolute; left: 0; top: 0; width: 100%;
    background: linear-gradient(180deg, var(--leaf-light) 0%, var(--leaf) 100%);
  }
  .band::after {
    content: ""; position: absolute; left: 0; right: 0; bottom: 2px;
    border-bottom: 2px dotted var(--paper);
  }
  .identity { position: absolute; right: 16px; top: 6px; text-align: left; }
  .identity-name {
    font-family: "Crimson Text", Georgia, serif; font-weight: 700;
    font-size: 21px; color: var(--leaf-dark); line-height: 1.05;
  }
  .identity-role {
    font-family: "Crimson Text", Georgia, serif; font-weight: 600;
    font-size: 15px; color: var(--paper); line-height: 1.1;
  }
  .brand { position: absolute; }
  .brand-mark { display: flex; align-items: center; gap: 6px; }
  .brand-square {
    width: 34px; height: 34px; border: 2px solid var(--paper); border-radius: 4px;
    background: rgba(255,255,255,0.15);
  }
  .brand-name {
    font-family: "Open Sans", Arial, sans-serif; font-weight: 700;
    font-size: 20px; color: var(--paper); letter-spacing: 1px;
  }
  .brand-tagline { margin-top: 6px; font-size: 7px; font-weight: 700; color: var(--leaf-dark); }
  .contact { position: absolute; left: 31px; }
  .contact-city { font-size: 11px; font-weight: 700; color: var(--leaf-dark); margin-bottom: 6px; line-height: 15px; }
  .contact-row { display: flex; font-size: 8.5px; line-height: 15px; }
  .contact-label { width: 40px; font-weight: 700; color: var(--ink); }
  .contact-value { color: var(--muted); }

  .card-front {
    left: 125px; top: 67px; width: 367px; height: 216px;
    background: radial-gradient(circle at 42% 38%, #ffffff 0%, var(--leaf-pale) 38%, var(--leaf-light) 100%);
  }
  .card-front .band { height: 53px; background: linear-gradient(180deg, var(--leaf-light), rgba(143,192,67,0.75)); }
  .card-front .band::after { display: none; }
  .card-back { left: 125px; top: 295px; width: 367px; height: 214px; }
  .card-back .band { height: 53px; }
  .card .brand { left: 31px; top: 17px; }
  .card .contact { top: 136px; }
  .card .contact-city { margin-bottom: 4px; }
  .card .contact-row { line-height: 13px; }

  .letterhead { left: 511px; top: 67px; width: 509px; height: 653px; }
  .letterhead .band { height: 77px; }
  .letterhead .brand { left: 36px; top: 16px; }
  .letterhead .contact { left: 36px; top: 576px; }

  .envelope { left: 542px; top: 307px; width: 423px; height: 281px; }
  .envelope .band { height: 77px; }
  .envelope .brand { left: 38px; top: 20px; }
  .envelope .contact { left: 38px; top: 200px; }
</style>
</head>
<body>
<div class="sheet">
  <div class="sheet-frame"></div>

  <section class="piece card card-front">
    <div class="band"></div>
    <div class="identity">
      <div class="identity-name">Greta Halloway</div>
      <div class="identity-role">Event Consultant</div>
    </div>
    <div class="brand">
      <div class="brand-mark"><span class="brand-square"></span><span class="brand-name">TRB</span></div>
      <div class="brand-tagline">Weddings &amp; Events by Greta</div>
    </div>
    <div class="contact">
      <div class="contact-city">Laguna Shores, CA</div>
      <div class="contact-row"><span class="contact-label">Phone</span><span class="contact-value">555.300.4790</span></div>
      <div class="contact-row"><span class="contact-label">Email</span><span class="contact-value">ghalloway@trbweddingsandevents.com</span></div>
      <div class="contact-row"><span class="contact-label">Web</span><span class="contact-value">www.trbweddingsandevents.com</span></div>
    </div>
  </section>

  <section class="piece card card-back">
    <div class="band"></div>
    <div class="identity">
      <div class="identity-name">Greta Halloway</div>
      <div class="identity-role">Event Consultant</div>
    </div>
    <div class="brand">
      <div class="brand-mark"><span class="brand-square"></span><span class="brand-name">TRB</span></div>
      <div class="brand-tagline">Weddings &amp; Events by Greta</div>
    </div>
    <div class="contact">
      <div class="contact-city">Laguna Shores, CA</div>
      <div class="contact-row"><span class="contact-label">Phone</span><span class="contact-value">555.300.4790</span></div>
      <div class="contact-row"><span class="contact-label">Email</span><span class="contact-value">ghalloway@trbweddingsandevents.com</span></div>
      <div class="contact-row"><span class="contact-label">Web</span><span class="contact-value">www.trbweddingsandevents.com</span></div>
    </div>
  </section>

  <section class="piece letterhead">
    <div class="band"></div>
    <div class="identity">
      <div class="identity-name">Greta Halloway</div>
      <div class="identity-role">Event Consultant</div>
    </div>
    <div class="brand">
      <div class="brand-mark"><span class="brand-square"></span><span class="brand-name">TRB</span></div>
      <div class="brand-tagline">Weddings &amp; Events by Greta</div>
    </div>
    <div class="contact">
      <div class="contact-city">Laguna Shores, CA</div>
      <div class="contact-row"><span class="contact-label">Phone</span><span class="contact-value">555.300.4790</span></div>
      <div class="contact-row"><span class="contact-label">Email</span><span class="contact-value">ghalloway@trbweddingsandevents.com</span></div>
      <div class="contact-row"><span class="contact-label">Web</span><span class="contact-value">www.trbweddingsandevents.com</span></div>
    </div>
  </section>

  <section class="piece envelope">
    <div class="band"></div>
    <div class="brand">
      <div class="brand-mark"><span class="brand-square"></span><span class="brand-name">TRB</span></div>
      <div class="brand-tagline">Weddings &amp; Events by Greta</div>
    </div>
    <div class="contact">
      <div class="contact-row"><span class="contact-label">Phone</span><span class="contact-value">555.300.4790</span></div>
      <div class="contact-row"><span class="contact-label">Email</span><span class="contact-value">ghalloway@trbweddingsandevents.com</span></div>
      <div class="contact-row"><span class="contact-label">Web</span><span class="contact-value">www.trbweddingsandevents.com</span></div>
    </div>
  </section>
</div>
</body>
</html>
```